redesign of my existing custom website into Wordpress based website

I need someone to redesign my current website into something more classy, simplistic, modern and on trend. I would like it set up on Wordpress in a way thats easy for me to make my own additions to blogs/price changes and promotion banners. I will also need a page that is password protected so members can login and have access to all my training videos and resources.
website is www.lilacnestfit.com.au

Target Market(s)

new mums

Industry/Entity Type

Fitness

Colors
33a6d7

Requirements
Must have
• chic, modern, stylish and simplistic.
• a call to action above the page fold
• mobile friendly conversion
• a pop up message as soon as someone enters my sight offering my free report
• a members page that is password protected containing 3 youtube videos and 6 pdf attachments as resources
• a home page
• a contact us page
• an about us page
• a blog page
• a store page
Nice to have
• some examples of my peers websites that I like:
• www.norahvale.com
• https://www.7qpz.com
• https://41withdaxford.com
Should not have
• anything gimmicky

```html
<!DOCTYPE html>
<html lang="en">
<head>
<meta charset="utf-8">
<title>Lilac Nest Fit – 12 Week Home Workout Program for Mums</title>
<link href="https://fonts.googleapis.com/css2?family=Open+Sans:ital,wght@0,400;0,600;0,700;0,800;1,600&display=swap" rel="stylesheet">
<style>
:root{
  --blue:#33a6d7;
  --blue-dark:#2a8cb8;
  --brand:#c2186f;
  --ink:#2f3236;
  --muted:#6b7077;
  --line:#dde1e5;
  --soft:#f4f5f7;
  --white:#ffffff;
  --hero-dark:#3b3f44;
}
*{box-sizing:border-box;margin:0;padding:0}
html,body{width:1200px;height:3922px;overflow:hidden}
body{position:relative;font-family:"Open Sans",Arial,sans-serif;color:var(--ink);background:var(--white);font-size:15px}
ul{list-style:none}
.wrap{position:relative;width:1002px;margin:0 auto}

/* header */
.site-header{height:92px;background:var(--white);border-top:5px solid var(--blue);position:relative;z-index:3}
.brand-badge{position:absolute;left:92px;top:-8px;width:192px;height:192px;border-radius:50%;background:var(--white);box-shadow:0 3px 10px rgba(0,0,0,.18);display:flex;align-items:center;justify-content:center;text-align:center}
.brand-name{font-weight:700;color:var(--brand);font-size:21px;line-height:1.15}
.main-nav{position:absolute;right:60px;top:30px;display:flex;gap:34px;align-items:center;font-size:14px;font-weight:700;text-transform:uppercase}
.main-nav a{color:var(--ink);text-decoration:none}
.main-nav .active{color:var(--blue)}
.cart{width:34px;height:34px;border-radius:50%;background:var(--blue);display:flex;align-items:center;justify-content:center}
.login{display:flex;gap:6px;align-items:center}

/* hero */
.hero{height:488px;position:relative;overflow:hidden}
.hero-photo{position:absolute;inset:0;background:linear-gradient(90deg,#33373c 0%,#44484d 45%,#8a8680 70%,#c6b7a6 100%)}
.hero-copy{position:absolute;left:99px;top:140px;color:var(--white);width:560px}
.hero-copy h1{font-size:40px;font-weight:800;line-height:1.22;text-transform:uppercase}
.hero-copy p{font-size:17px;margin-top:22px;line-height:1.6;color:#e4e6e8}
.hero-actions{display:flex;gap:16px;margin-top:26px}
.btn-pill{display:inline-flex;align-items:center;gap:8px;height:40px;padding:0 26px;border-radius:20px;font-size:14px;font-weight:700;text-transform:uppercase;color:var(--white);background:var(--blue)}
.btn-ghost{background:transparent;border:2px solid var(--white)}
.slide-arrow{position:absolute;top:318px;width:26px;height:40px}
.slide-arrow.prev{left:30px}.slide-arrow.next{right:30px}

/* features */
.features{height:400px;background:var(--soft);text-align:center;padding-top:50px}
.section-title{font-size:30px;font-weight:700;color:var(--ink)}
.feature-row{display:flex;justify-content:center;gap:110px;margin-top:46px}
.feature{width:162px}
.feature-ring{width:162px;height:162px;border-radius:50%;border:3px solid #c9ced3;background:var(--white);display:flex;align-items:center;justify-content:center}
.feature h3{margin-top:36px;font-size:19px;font-weight:600}

/* program */
.program{height:432px;background:var(--white);padding-top:60px}
.program .wrap{display:flex;justify-content:space-between}
.program-copy h2{font-size:29px;font-weight:700;line-height:1.3;width:470px}
.ticks{margin-top:30px}
.ticks li{display:flex;align-items:center;gap:14px;font-size:13px;color:var(--muted);height:34px}
.tick{flex:none;width:18px;height:18px}
.video{width:500px;height:334px;margin-top:11px;position:relative;background:linear-gradient(135deg,#3a3a3d,#6a5a5f 55%,#2d2e31)}
.video-bar{position:absolute;left:0;right:0;top:0;height:34px;background:rgba(0,0,0,.55);color:var(--white);font-size:13px;display:flex;align-items:center;padding:0 12px}
.video-play{position:absolute;left:50%;top:50%;transform:translate(-50%,-50%)}

/* opt-in */
.optin{height:339px;background:var(--blue);color:var(--white)}
.optin .wrap{display:flex;justify-content:space-between;padding-top:65px}
.optin-copy h2{font-size:29px;font-weight:700;line-height:1.25}
.optin-copy p{font-size:13px;margin-top:22px;line-height:1.55;width:340px;opacity:.9}
.optin-copy .free{font-style:italic;font-weight:600;font-size:20px;margin-top:34px}
.optin-form{width:491px;height:251px;border:3px solid rgba(255,255,255,.85);margin-top:-26px;padding:26px 28px}
.field{height:40px;border:1px solid rgba(255,255,255,.8);border-radius:3px;padding:0 14px;display:flex;align-items:center;font-size:13px;color:rgba(255,255,255,.85);margin-bottom:20px}
.agree{display:flex;align-items:center;gap:10px;font-size:13px}
.agree span.box{width:14px;height:14px;border:1px solid var(--white);background:transparent}
.form-btn{margin-top:22px;height:44px;border-radius:22px;background:var(--white);color:var(--blue-dark);font-weight:700;font-size:14px;display:flex;align-items:center;justify-content:center;text-transform:uppercase}

/* included */
.included{height:458px;background:var(--soft);padding-top:52px}
.included .wrap{display:flex;gap:120px}
.product-shot{width:390px;height:366px;margin-left:58px;background:linear-gradient(140deg,#2b2d35,#c9487f 55%,#f1e3ea)}
.included-copy h2{font-size:29px;font-weight:700;margin-top:22px}

/* different */
.different{height:261px;background:var(--white);text-align:center;padding-top:30px}
.diff-row{display:flex;justify-content:center;gap:40px;margin-top:38px}
.diff{width:210px}
.diff h3{font-size:16px;font-weight:600;line-height:1.45;margin-top:14px}

/* equipment */
.equipment{height:406px;position:relative;background:var(--soft)}
.equipment-photo{position:absolute;right:0;top:0;width:600px;height:406px;background:linear-gradient(90deg,var(--soft) 0%,#e8e4e6 25%,#d8cfd3 60%,#cfc5bf 100%)}
.equipment-copy{position:absolute;left:99px;top:68px}
.equipment-copy h2{font-size:29px;font-weight:700}

/* news */
.news{height:527px;background:var(--white);padding-top:50px;text-align:center}
.news-grid{display:flex;justify-content:space-between;margin-top:38px;text-align:left}
.post{width:314px}
.post-thumb{height:201px;position:relative}
.post-date{position:absolute;left:0;bottom:-2px;width:50px;height:62px;background:var(--blue);color:var(--white);text-align:center;font-weight:700;font-size:22px;padding-top:6px;line-height:1.1}
.post-date small{display:block;font-size:11px;font-weight:600;text-transform:uppercase}
.post h3{font-size:16px;font-weight:700;margin-top:30px}
.post p{font-size:11px;color:var(--muted);margin-top:12px;line-height:1.55}
.post-meta{display:flex;gap:20px;margin-top:26px;font-size:11px;color:var(--muted)}
.post-meta span{display:flex;gap:6px;align-items:center}

/* testimonial */
.testimonial{height:212px;background:var(--blue);color:var(--white);position:relative}
.testimonial .avatar{position:absolute;left:110px;top:24px;width:125px;height:125px;border-radius:50%;border:4px solid var(--white);background:linear-gradient(160deg,#8e9aa5,#57626d)}
.testimonial .rule{position:absolute;left:270px;top:28px;width:1px;height:150px;background:rgba(255,255,255,.4)}
.testimonial blockquote{position:absolute;left:308px;top:36px;width:842px;font-size:13px;font-style:italic;line-height:1.6;opacity:.92}
.testimonial cite{position:absolute;left:308px;top:140px;font-style:normal;font-weight:600;font-size:17px}
.testimonial .slide-arrow{top:86px}

/* footer */
.site-footer{height:307px;background:var(--soft);position:relative}
.footer-brand{position:absolute;left:92px;top:40px;width:190px;height:136px;display:flex;align-items:center;gap:12px}
.footer-brand .dot{width:16px;height:16px;border-radius:50%;background:var(--brand)}
.fcol{position:absolute;top:44px}
.fcol h4{font-size:15px;font-weight:700;margin-bottom:14px}
.fcol li{font-size:11px;color:var(--muted);line-height:1.75}
.fcol p{font-size:11px;color:var(--muted);line-height:1.6;width:240px}
.news-field{width:250px;height:28px;border:1px solid var(--line);background:var(--white);margin-top:12px;font-size:10px;color:#999;padding:6px 8px}
.news-btn{margin-top:12px;width:84px;height:24px;border:1px solid var(--muted);font-size:10px;display:flex;align-items:center;justify-content:center;color:var(--muted)}
.contact li{display:flex;gap:10px;align-items:flex-start;margin-bottom:14px}
.footer-bottom{position:absolute;left:0;right:0;top:241px;border-top:1px solid var(--line);height:66px;padding:0 92px;display:flex;align-items:center;justify-content:space-between;font-size:10px;color:var(--muted)}
.socials{display:flex;gap:10px;align-items:center}
.socials i{width:22px;height:22px;border-radius:50%;border:1px solid #bfc4c9;display:block}

/* welcome pop-up */
.overlay{position:absolute;inset:0;background:rgba(20,24,28,.42);z-index:10}
.welcome{position:absolute;z-index:11;left:280px;top:104px;width:640px;height:640px;border-radius:50%;background:var(--white);border:8px solid var(--blue);text-align:center}
.welcome .brand-name{position:absolute;left:0;right:0;top:58px;font-size:26px}
.welcome p{position:absolute;left:130px;width:364px;top:146px;font-size:12px;line-height:2.05;color:var(--ink)}
.welcome .btn-pill{position:absolute;left:224px;top:494px;width:176px;height:52px;border-radius:26px;justify-content:center}
.welcome .close{position:absolute;left:0;right:0;top:598px;font-size:12px;text-transform:uppercase;color:var(--muted)}
</style>
</head>
<body>

<header class="site-header">
  <div class="brand-badge"><span class="brand-name">Lilac Nest<br>Fit</span></div>
  <nav class="main-nav">
    <a class="active" href="#">Home</a>
    <a href="#">About us</a>
    <a href="#">Program</a>
    <a href="#">Blog</a>
    <a href="#">Shop</a>
    <a href="#">Contact us</a>
    <span class="cart"><svg width="18" height="16" viewBox="0 0 18 16"><path d="M1 1h3l2 9h9l2-6H5" fill="none" stroke="#fff" stroke-width="1.8"/><circle cx="7" cy="14" r="1.4" fill="#fff"/><circle cx="14" cy="14" r="1.4" fill="#fff"/></svg></span>
    <span class="login"><svg width="12" height="14" viewBox="0 0 12 14"><rect x="1" y="6" width="10" height="8" fill="#33a6d7"/><path d="M3 6V4a3 3 0 0 1 6 0v2" fill="none" stroke="#33a6d7" stroke-width="1.6"/></svg>Login</span>
  </nav>
</header>

<section class="hero">
  <div class="hero-photo" role="img" aria-label="Smiling young mum in a green training top, photographed in a bright home setting"></div>
  <div class="hero-copy">
    <h1>12 Week Home Workout<br>Program for Mums</h1>
    <p>Your purchase of the Home Workout Program<br>Pack comes loaded with everything you need.</p>
    <div class="hero-actions">
      <span class="btn-pill">Watch now <svg width="12" height="12" viewBox="0 0 12 12"><circle cx="6" cy="6" r="5.5" fill="#fff"/><path d="M5 3.5 8 6 5 8.5Z" fill="#33a6d7"/></svg></span>
      <span class="btn-pill btn-ghost">Buy now</span>
    </div>
  </div>
  <svg class="slide-arrow prev" viewBox="0 0 26 40"><path d="M20 4 6 20l14 16" fill="none" stroke="#fff" stroke-width="4"/></svg>
  <svg class="slide-arrow next" viewBox="0 0 26 40"><path d="M6 4l14 16L6 36" fill="none" stroke="#fff" stroke-width="4"/></svg>
</section>

<section class="features">
  <h2 class="section-title">Lose your baby weight and bounce back into shape!</h2>
  <div class="feature-row">
    <div class="feature"><div class="feature-ring"><svg width="70" height="70" viewBox="0 0 70 70" fill="none" stroke="#33a6d7" stroke-width="4"><circle cx="35" cy="35" r="12"/><path d="M35 8v10M35 52v10M8 35h10M52 35h10M16 16l7 7M47 47l7 7M54 16l-7 7M23 47l-7 7"/></svg></div><h3>Mindfulness</h3></div>
    <div class="feature"><div class="feature-ring"><svg width="70" height="70" viewBox="0 0 70 70"><path d="M35 20c-8-6-24-4-24 14 0 14 10 28 18 28 3 0 4-2 6-2s3 2 6 2c8 0 18-14 18-28 0-18-16-20-24-14Z" fill="#33a6d7"/><path d="M35 20c0-6 3-10 8-12" fill="none" stroke="#33a6d7" stroke-width="3"/><circle cx="50" cy="50" r="9" fill="#fff" stroke="#33a6d7" stroke-width="3"/><path d="m46 50 3 3 5-6" fill="none" stroke="#33a6d7" stroke-width="3"/></svg></div><h3>Nutrition</h3></div>
    <div class="feature"><div class="feature-ring"><svg width="80" height="50" viewBox="0 0 80 50"><rect x="4" y="12" width="10" height="26" rx="2" fill="#33a6d7"/><rect x="16" y="6" width="10" height="38" rx="2" fill="#33a6d7"/><rect x="26" y="22" width="28" height="6" fill="#33a6d7"/><rect x="54" y="6" width="10" height="38" rx="2" fill="#33a6d7"/><rect x="66" y="12" width="10" height="26" rx="2" fill="#33a6d7"/></svg></div><h3>Workout</h3></div>
    <div class="feature"><div class="feature-ring"><svg width="70" height="70" viewBox="0 0 70 70"><rect x="10" y="30" width="12" height="28" rx="2" fill="#33a6d7"/><path d="M26 32 38 12c4-2 8 1 7 6l-3 10h14c4 0 6 4 5 7l-5 20c-1 3-3 4-6 4H26Z" fill="#33a6d7"/></svg></div><h3>Motivation</h3></div>
  </div>
</section>

<section class="program">
  <div class="wrap">
    <div class="program-copy">
      <h2>12 week Home Workout Program For Mums!</h2>
      <ul class="ticks">
        <li><svg class="tick" viewBox="0 0 18 18"><circle cx="9" cy="9" r="9" fill="#33a6d7"/><path d="m5 9 3 3 5-6" fill="none" stroke="#fff" stroke-width="2"/></svg>12 week, cardio and resistance circuit training program</li>
        <li><svg class="tick" viewBox="0 0 18 18"><circle cx="9" cy="9" r="9" fill="#33a6d7"/><path d="m5 9 3 3 5-6" fill="none" stroke="#fff" stroke-width="2"/></svg>Follow along workout DVD</li>
        <li><svg class="tick" viewBox="0 0 18 18"><circle cx="9" cy="9" r="9" fill="#33a6d7"/><path d="m5 9 3 3 5-6" fill="none" stroke="#fff" stroke-width="2"/></svg>Workout equipment delivered to your front door</li>
        <li><svg class="tick" viewBox="0 0 18 18"><circle cx="9" cy="9" r="9" fill="#33a6d7"/><path d="m5 9 3 3 5-6" fill="none" stroke="#fff" stroke-width="2"/></svg>Weekly coaching emails</li>
        <li><svg class="tick" viewBox="0 0 18 18"><circle cx="9" cy="9" r="9" fill="#33a6d7"/><path d="m5 9 3 3 5-6" fill="none" stroke="#fff" stroke-width="2"/></svg>Accountability charts &amp; program cards</li>
        <li><svg class="tick" viewBox="0 0 18 18"><circle cx="9" cy="9" r="9" fill="#33a6d7"/><path d="m5 9 3 3 5-6" fill="none" stroke="#fff" stroke-width="2"/></svg>Family friendly healthy recipes</li>
        <li><svg class="tick" viewBox="0 0 18 18"><circle cx="9" cy="9" r="9" fill="#33a6d7"/><path d="m5 9 3 3 5-6" fill="none" stroke="#fff" stroke-width="2"/></svg>Healthy eating guidelines</li>
      </ul>
    </div>
    <div class="video" role="img" aria-label="Video still of a mum exercising on a living room floor beside her baby">
      <div class="video-bar">Lose your baby weight and get back into shape!</div>
      <svg class="video-play" width="64" height="46" viewBox="0 0 64 46"><rect width="64" height="46" rx="12" fill="rgba(20,20,20,.8)"/><path d="M26 14v18l15-9Z" fill="#fff"/></svg>
    </div>
  </div>
</section>

<section class="optin">
  <div class="wrap">
    <div class="optin-copy">
      <h2>Get your<br>FREE top 10<br>Baby Belly Blasting Tips</h2>
      <p>Join our email list for a flatter post-baby tummy starting today, tips you can start straight away.</p>
      <div class="free">for free today!</div>
    </div>
    <form class="optin-form">
      <div class="field">Name</div>
      <div class="field">Email</div>
      <div class="agree"><span class="box"></span>I agree to Terms &amp; Conditions</div>
      <div class="form-btn">Get it free now!</div>
    </form>
  </div>
</section>

<section class="included">
  <div class="wrap">
    <div class="product-shot" role="img" aria-label="Program pack with workout DVD, step platform and recipe guide booklets"></div>
    <div class="included-copy">
      <h2>What's included in the program?</h2>
      <ul class="ticks">
        <li><svg class="tick" viewBox="0 0 18 18"><circle cx="9" cy="9" r="9" fill="#33a6d7"/><path d="m5 9 3 3 5-6" fill="none" stroke="#fff" stroke-width="2"/></svg>Our unique 3 stage, 12 week training program</li>
        <li><svg class="tick" viewBox="0 0 18 18"><circle cx="9" cy="9" r="9" fill="#33a6d7"/><path d="m5 9 3 3 5-6" fill="none" stroke="#fff" stroke-width="2"/></svg>Full instructional Workout DVD and program cards for each program</li>
        <li><svg class="tick" viewBox="0 0 18 18"><circle cx="9" cy="9" r="9" fill="#33a6d7"/><path d="m5 9 3 3 5-6" fill="none" stroke="#fff" stroke-width="2"/></svg>Weekly accountability charts</li>
        <li><svg class="tick" viewBox="0 0 18 18"><circle cx="9" cy="9" r="9" fill="#33a6d7"/><path d="m5 9 3 3 5-6" fill="none" stroke="#fff" stroke-width="2"/></svg>Weekly coaching emails</li>
        <li><svg class="tick" viewBox="0 0 18 18"><circle cx="9" cy="9" r="9" fill="#33a6d7"/><path d="m5 9 3 3 5-6" fill="none" stroke="#fff" stroke-width="2"/></svg>Funky exercise equipment for your home</li>
        <li><svg class="tick" viewBox="0 0 18 18"><circle cx="9" cy="9" r="9" fill="#33a6d7"/><path d="m5 9 3 3 5-6" fill="none" stroke="#fff" stroke-width="2"/></svg>Nutritionist approved healthy eating guide</li>
        <li><svg class="tick" viewBox="0 0 18 18"><circle cx="9" cy="9" r="9" fill="#33a6d7"/><path d="m5 9 3 3 5-6" fill="none" stroke="#fff" stroke-width="2"/></svg>Healthy family favourites recipe ebook</li>
      </ul>
    </div>
  </div>
</section>

<section class="different">
  <h2 class="section-title">Why our program is different</h2>
  <div class="diff-row">
    <div class="diff"><svg width="56" height="52" viewBox="0 0 56 52" fill="none" stroke="#33a6d7" stroke-width="4"><path d="M30 8H6v40h40V24"/><path d="M22 34l4-10 20-20 6 6-20 20Z" fill="#33a6d7"/></svg><h3>Specially designed for<br>Mums</h3></div>
    <div class="diff"><svg width="80" height="44" viewBox="0 0 80 44"><rect x="4" y="12" width="8" height="20" fill="#33a6d7"/><rect x="16" y="4" width="8" height="36" fill="#33a6d7"/><rect x="24" y="19" width="32" height="6" fill="#33a6d7"/><rect x="56" y="4" width="8" height="36" fill="#33a6d7"/><rect x="68" y="12" width="8" height="20" fill="#33a6d7"/></svg><h3>Workout equipment included<br>so you can train from home</h3></div>
    <div class="diff"><svg width="70" height="48" viewBox="0 0 70 48"><circle cx="24" cy="20" r="7" fill="#33a6d7"/><circle cx="36" cy="15" r="8" fill="#33a6d7"/><circle cx="48" cy="20" r="7" fill="#33a6d7"/><path d="M4 24h62c0 14-12 22-31 22S4 38 4 24Z" fill="#33a6d7"/></svg><h3>Delicious low fat family<br>friendly recipes</h3></div>
    <div class="diff"><svg width="60" height="52" viewBox="0 0 60 52"><path d="M20 10V4h20v6" fill="none" stroke="#33a6d7" stroke-width="4"/><rect x="2" y="10" width="56" height="40" rx="4" fill="#33a6d7"/><path d="M26 20h8v8h8v8h-8v8h-8v-8h-8v-8h8Z" fill="#fff"/></svg><h3>Caters for mums at all stages<br>of post baby recovery</h3></div>
  </div>
</section>

<section class="equipment">
  <div class="equipment-photo" role="img" aria-label="Mum kneeling on a lounge room floor doing a dumbbell exercise while her toddler plays alongside"></div>
  <div class="equipment-copy">
    <h2>Already have the equipment you need?</h2>
    <ul class="ticks">
      <li><svg class="tick" viewBox="0 0 18 18"><circle cx="9" cy="9" r="9" fill="#33a6d7"/><path d="m5 9 3 3 5-6" fill="none" stroke="#fff" stroke-width="2"/></svg>Our 3 stage, 12 week training program</li>
      <li><svg class="tick" viewBox="0 0 18 18"><circle cx="9" cy="9" r="9" fill="#33a6d7"/><path d="m5 9 3 3 5-6" fill="none" stroke="#fff" stroke-width="2"/></svg>Full instructional Workout DVD for each program</li>
      <li><svg class="tick" viewBox="0 0 18 18"><circle cx="9" cy="9" r="9" fill="#33a6d7"/><path d="m5 9 3 3 5-6" fill="none" stroke="#fff" stroke-width="2"/></svg>Weekly accountability charts</li>
      <li><svg class="tick" viewBox="0 0 18 18"><circle cx="9" cy="9" r="9" fill="#33a6d7"/><path d="m5 9 3 3 5-6" fill="none" stroke="#fff" stroke-width="2"/></svg>Weekly coaching emails</li>
      <li><svg class="tick" viewBox="0 0 18 18"><circle cx="9" cy="9" r="9" fill="#33a6d7"/><path d="m5 9 3 3 5-6" fill="none" stroke="#fff" stroke-width="2"/></svg>Nutritionist approved healthy eating guidelines</li>
      <li><svg class="tick" viewBox="0 0 18 18"><circle cx="9" cy="9" r="9" fill="#33a6d7"/><path d="m5 9 3 3 5-6" fill="none" stroke="#fff" stroke-width="2"/></svg>Healthy family favourites recipe ebook</li>
    </ul>
  </div>
</section>

<section class="news">
  <h2 class="section-title">Top News</h2>
  <div class="wrap news-grid">
    <article class="post">
      <div class="post-thumb" role="img" aria-label="Toddler climbing onto an aerobic step in a living room" style="background:linear-gradient(135deg,#5a4a4e,#b7546e 55%,#d9c9c4)"><div class="post-date">25<small>Sep</small></div></div>
      <h3>The benefits of training in the morning</h3>
      <p>Still finding it hard to fit a session in? Early starts give mums a calm window before the busy day begins.</p>
      <div class="post-meta"><span>&#9679; Owen Halloway</span><span>&#9679; 3 Comments</span></div>
    </article>
    <article class="post">
      <div class="post-thumb" role="img" aria-label="Bowl of creamy orange pumpkin soup" style="background:radial-gradient(circle at 50% 55%,#d99a2b 0,#c88422 32%,#e9e5df 34%,#cfc8bf 100%)"><div class="post-date">23<small>Sep</small></div></div>
      <h3>Creamy Pumpkin Soup</h3>
      <p>I made this soup the other day and OMG, it was so creamy and delicious. The whole family loved it too.</p>
      <div class="post-meta"><span>&#9679; Owen Halloway</span><span>&#9679; 3 Comments</span></div>
    </article>
    <article class="post">
      <div class="post-thumb" role="img" aria-label="Mum doing a floor exercise on a mat in a lounge room" style="background:linear-gradient(135deg,#3b3a40,#7a6e72 50%,#b3a9a6)"><div class="post-date">23<small>Sep</small></div></div>
      <h3>Greta's 10 exercise lounge room...</h3>
      <p>Get the blood pumping with this short circuit, easy to do in the lounge while the little one plays nearby.</p>
      <div class="post-meta"><span>&#9679; Owen Halloway</span><span>&#9679; 3 Comments</span></div>
    </article>
  </div>
</section>

<section class="testimonial">
  <svg class="slide-arrow prev" viewBox="0 0 26 40"><path d="M18 8 8 20l10 12" fill="none" stroke="#fff" stroke-width="3"/></svg>
  <div class="avatar" role="img" aria-label="Portrait of the reviewer"></div>
  <div class="rule"></div>
  <blockquote>The program fitted around naps, feeds and school runs, and I never once needed to leave the house. The weekly emails kept me on track, the recipes became family staples, and after twelve weeks I felt stronger than before my pregnancy. I can't recommend it enough to new mums.</blockquote>
  <cite>- Marcel Doucet</cite>
  <svg class="slide-arrow next" viewBox="0 0 26 40"><path d="M8 8l10 12L8 32" fill="none" stroke="#fff" stroke-width="3"/></svg>
</section>

<footer class="site-footer">
  <div class="footer-brand"><span class="dot"></span><span class="brand-name">Lilac Nest Fit</span></div>
  <div class="fcol" style="left:382px">
    <h4>Information</h4>
    <ul><li>Home</li><li>About Us</li><li>Program</li><li>Blog</li><li>Shop</li><li>Contact Us</li></ul>
  </div>
  <div class="fcol" style="left:565px">
    <h4>Newsletter Subscription</h4>
    <p>Register your email address to get information about us</p>
    <div class="news-field">Email address</div>
    <div class="news-btn">Subscribe</div>
  </div>
  <div class="fcol contact" style="left:892px">
    <h4>Contact Us</h4>
    <ul>
      <li><svg width="10" height="14" viewBox="0 0 10 14"><path d="M5 0a5 5 0 0 1 5 5c0 4-5 9-5 9S0 9 0 5a5 5 0 0 1 5-5Z" fill="#33a6d7"/><circle cx="5" cy="5" r="2" fill="#fff"/></svg>14 Wren Lane,<br>Harbour Vale</li>
      <li><svg width="12" height="12" viewBox="0 0 12 12"><path d="M2 0l3 3-1.5 2a7 7 0 0 0 3.5 3.5L9 7l3 3-2 2C5 12 0 7 0 2Z" fill="#33a6d7"/></svg>+1 800 555 0147</li>
      <li><svg width="13" height="10" viewBox="0 0 13 10"><rect width="13" height="10" fill="#33a6d7"/><path d="m0 0 6.5 5L13 0" fill="none" stroke="#fff"/></svg>hello@lilacnestfit.com.au</li>
    </ul>
  </div>
  <div class="footer-bottom">
    <span>Copyright © 2015 Lilac Nest Fit. All rights reserved.</span>
    <div class="socials"><i></i><i></i><i></i><i></i><span>CST</span></div>
  </div>
</footer>

<div class="overlay"></div>
<div class="welcome" role="dialog" aria-label="Welcome">
  <span class="brand-name">Lilac Nest Fit</span>
  <p>After a life time of competitive sports and as a qualified personal trainer, I thought I knew exactly what it would take to get my body back after having babies. I put on a massive 30 kgs with my first pregnancy and found myself in a situation for the first time in my life where I had to lose a lot of weight.</p>
  <span class="btn-pill">Enter site</span>
  <span class="close">Close</span>
</div>

</body>
</html>
```